Delvin & Associates - London New Letting and Property Management Company *

Delvin & Associates LTD is a new company based in London, and works with brand new residential property in the city centre.

We are aiming to have 1000 new properties a year.

We are looking for something modern and minimalistic :
Logo ,Monogram, Paper Head and Business Card.

Target Market(s)

Internation landlords

Industry/Entity Type

Real Estate

Logo Text

Delvin & Associates

Colors

Designer to choose colors to be used in the design.

Requirements
Nice to have
• A particular monogram with "DA"
Should not have
• Little House over the logo

```html
<!DOCTYPE html>
<html lang="en">
<head>
<meta charset="utf-8">
<title>Delvin &amp; Associates LTD – Envelopes</title>
<link rel="stylesheet" href="https://fonts.googleapis.com/css2?family=Crimson+Pro:wght@600&family=Open+Sans:wght@400&display=swap">
<style>
  :root {
    --bg: #f4f4f4;
    --envelope-grey: #e6e6e6;
    --envelope-white: #f8f8fa;
    --window: #fafafa;
    --brand-blue: #0f4c6e;
    --ink: #2b2b2b;
    --fold-line: #cfcfd4;
    --mark-faint: #efefef;
  }
  * { box-sizing: border-box; margin: 0; padding: 0; }
  html, body { width: 1200px; height: 1000px; overflow: hidden; }
  body { background: var(--bg); position: relative; font-family: "Open Sans", sans-serif; }

  .envelope { position: absolute; }

  /* Front envelope with address window */
  .envelope--front {
    left: 80px; top: 50px; width: 850px; height: 430px;
    background: var(--envelope-grey);
    border: 1px solid #d4d4d4;
    overflow: hidden;
  }
  .front__decoration {
    position: absolute; left: 180px; top: 90px;
    width: 210px; height: 210px; border-radius: 50%;
    background: var(--mark-faint);
  }
  .front__window {
    position: absolute; right: 50px; top: 190px;
    width: 290px; height: 180px; border-radius: 34px;
    background: var(--window);
  }
  .front__brand {
    position: absolute; left: 40px; bottom: 26px;
    font-family: "Crimson Pro", serif; font-weight: 600;
    font-size: 26px; line-height: 1.1; color: var(--brand-blue);
  }

  /* Back envelope with flap */
  .envelope--back {
    left: 260px; top: 490px; width: 880px; height: 450px;
    background: var(--envelope-white);
    border: 1px solid #dedee2;
  }
  .back__flap { position: absolute; left: 0; top: 0; width: 880px; height: 450px; }
  .back__flap-text {
    position: absolute; left: 0; top: 20px; width: 880px; text-align: center;
  }
  .company-name {
    font-family: "Crimson Pro", serif; font-weight: 600;
    font-size: 56px; line-height: 1; color: var(--brand-blue);
  }
  .tagline { margin-top: 10px; font-size: 21px; color: var(--ink); }
  .address { margin-top: 4px; font-size: 21px; line-height: 1.3; color: var(--brand-blue); font-style: normal; }
  .back__brand {
    position: absolute; left: 0; width: 880px; top: 330px; text-align: center;
    font-family: "Crimson Pro", serif; font-weight: 600;
    font-size: 18px; color: var(--ink);
  }
</style>
</head>
<body>

  <section class="envelope envelope--front" aria-label="Windowed envelope front">
    <div class="front__decoration" aria-hidden="true"></div>
    <div class="front__window"></div>
    <p class="front__brand">Delvin &amp; Associates</p>
  </section>

  <section class="envelope envelope--back" aria-label="Envelope back with flap">
    <svg class="back__flap" viewBox="0 0 880 450" aria-hidden="true">
      <path d="M0,440 Q300,120 440,200 Q580,120 880,440" fill="none" stroke="var(--fold-line)" stroke-width="1.2"/>
      <path d="M0,0 Q440,600 880,0 Z" fill="var(--envelope-grey)"/>
    </svg>
    <div class="back__flap-text">
      <h1 class="company-name">Delvin &amp; Associates LTD</h1>
      <p class="tagline">brand new residential properties</p>
      <address class="address">
        14 Harrow Mews, Kensal Rise, London<br>
        NW10 3QX<br>
        United Kingdom of Great Britain
      </address>
    </div>
    <p class="back__brand">Delvin &amp; Associates</p>
  </section>

</body>
</html>
```